Poster for Billard- & Sportsbar: "Specials"

Hi,
I Need a Poster for my Billard- & Sportsbar, which Shows our weekly Specials.
The size should be DinA0 (84 x 118.8 cm). Please notice the print instructions attached.

Text Information for the Poster:

"Wochenhighlights

Dienstag: Flatrate-Billard
Für nur 5€ (7€) pro Person den ganzen Abend Pool-Billard (Snooker)spielen

Mittwoch: Studenten-Nacht
Studenten & Auszubildende spielen Pool-Billard für nur 4,50€ die Stunde

Donnerstag: Snooker-Donnerstag
Donnerstags kostet der Snooker Tisch gerade mal 5€ die Stunde

Freitag: Kesselgold-Special
6 Talhof Kesselgold-Pils für nur 11,99€

Samstag: Schau dein Wunschsspiel
Reserviere die Private Lounge und schaue das Staffelrunde-Spiel deiner Wahl. Reservierungsgebühr: 10€, ab 6 Personen kostenlos.
(Gilt auch für EP, VKT-Pokal & Englische Wochen)

Sonntag: Play for Free
Wer vor 18:00 Uhr mit dem Spielen beginnt, spielt den ganzen Abend umsonst!"

You can choose the Colors free. If you use Pictures, take care that they are free or send me the link where they can get bought.

I have uploaded the logo of my bar. You can use it in the poster, but please not too big.

You can maybe use the Colors of the logo as main Colors. But it is not a must.

If you have questions, just contact me!

Thank you in advance!

Jorik

A short update: Please mind, that it is the most important Thing, that the customers can read the Special offers! Thank you

```html
<!DOCTYPE html>
<html lang="de">
<head>
<meta charset="utf-8">
<title>Kugelhaus – Wochenhighlights</title>
<link href="https://fonts.googleapis.com/css2?family=Jost:ital,wght@0,400;0,500;0,700;0,800;1,500;1,600&family=Archivo+Black&display=swap" rel="stylesheet">
<style>
  :root {
    --page: #ffffff;
    --felt: #12a24a;
    --felt-shade: #0a7a34;
    --ink: #ffffff;
    --label-bg: #ffffff;
    --label-ink: #0f8a3e;
    --brand-ink: #1c1c1c;
    --cue-tone: #b58a5e;
    --cue-tone-light: #d9c39a;
    --ball-tone: rgba(200, 170, 90, .35);
    --snooker-tone: rgba(190, 30, 40, .55);
  }
  * { margin: 0; padding: 0; box-sizing: border-box; }
  html, body { width: 1200px; height: 900px; overflow: hidden; background: var(--page); }
  .canvas { position: relative; width: 1200px; height: 900px; }

  .poster {
    position: absolute; left: 300px; top: 27px; width: 600px; height: 848px;
    background: var(--felt);
    box-shadow: 0 1px 4px rgba(0,0,0,.35);
    overflow: hidden;
    font-family: "Jost", "Futura", sans-serif;
    color: var(--ink);
  }
  .table-backdrop {
    position: absolute; left: 0; top: 470px; width: 600px; height: 378px;
    background: linear-gradient(180deg, rgba(10,122,52,0) 0%, rgba(10,122,52,.55) 25%, rgba(8,110,46,.5) 70%, rgba(10,122,52,.3) 100%);
  }

  .brand { position: absolute; left: 0; top: 16px; width: 600px; text-align: center; color: var(--brand-ink); }
  .brand-name { font-weight: 800; font-size: 38px; letter-spacing: 1px; line-height: 38px; }
  .brand-tagline { font-weight: 500; font-size: 6.5px; letter-spacing: 1px; margin-left: 150px; line-height: 8px; }

  .headline {
    position: absolute; left: 0; top: 94px; width: 600px; text-align: center;
    font-style: italic; font-weight: 600; font-size: 50px; letter-spacing: -0.5px; line-height: 56px;
  }

  .art-area { position: absolute; }
  .art-cue {
    left: 50px; top: 157px; width: 500px; height: 9px;
    background: linear-gradient(90deg, var(--cue-tone) 0%, var(--cue-tone-light) 100%);
    opacity: .7;
  }
  .art-balls { background: var(--ball-tone); }
  .art-snooker { background: var(--snooker-tone); }

  .special { position: absolute; left: 0; width: 600px; }
  .day-label {
    position: absolute; left: 0; width: 132px; height: 26px;
    background: var(--label-bg); color: var(--label-ink);
    font-family: "Archivo Black", sans-serif; font-size: 15px; line-height: 26px; padding-left: 20px;
    white-space: nowrap;
  }
  .day-label.is-wide { width: 158px; }
  .special-body { position: absolute; left: 173px; top: -8px; }
  .special-title { font-style: italic; font-weight: 500; font-size: 24px; line-height: 34px; }
  .special-text { font-weight: 500; font-size: 19px; line-height: 19.5px; white-space: nowrap; }
  .special-note { font-size: 13.5px; }
</style>
</head>
<body>
<div class="canvas">
  <main class="poster">
    <div class="table-backdrop" role="img" aria-label="Blasses Foto eines Billardtischs im Hintergrund"></div>

    <header class="brand">
      <div class="brand-name">KUGELHAUS</div>
      <div class="brand-tagline">BILLARD - SPORTSBAR - LOUNGE</div>
    </header>

    <h1 class="headline">WOCHENHIGHLIGHTS</h1>
    <div class="art-area art-cue" role="img" aria-label="Illustration eines Billard-Queues"></div>

    <div class="art-area art-balls" role="img" aria-label="Illustration: Poolkugeln und Dreieck" style="left:412px;top:178px;width:145px;height:78px"></div>
    <div class="art-area art-balls" role="img" aria-label="Illustration: drei Poolkugeln" style="left:512px;top:376px;width:50px;height:56px"></div>
    <div class="art-area art-balls" role="img" aria-label="Illustration: zwei Poolkugeln" style="left:518px;top:488px;width:44px;height:68px"></div>
    <div class="art-area art-balls" role="img" aria-label="Illustration: Poolkugel und Spielkugel" style="left:510px;top:628px;width:46px;height:68px"></div>
    <div class="art-area art-snooker" role="img" aria-label="Illustration: rote Snookerkugeln im Dreieck" style="left:55px;top:762px;width:85px;height:56px"></div>

    <section class="special" style="top:213px">
      <div class="day-label">DIENSTAG</div>
      <div class="special-body">
        <h2 class="special-title">Flatrate-Billard</h2>
        <p class="special-text">Für nur 5€ (7€) pro Person<br>den ganzen Abend Pool-Billard (Snooker)spielen</p>
      </div>
    </section>

    <section class="special" style="top:306px">
      <div class="day-label">MITTWOCH</div>
      <div class="special-body">
        <h2 class="special-title">Studenten-Nacht</h2>
        <p class="special-text">Studenten &amp; Auszubildende spielen Pool-Billard<br>für nur 4,50€ die Stunde</p>
      </div>
    </section>

    <section class="special" style="top:398px">
      <div class="day-label is-wide">DONNERSTAG</div>
      <div class="special-body">
        <h2 class="special-title">Snooker-Donnerstag</h2>
        <p class="special-text">Donnerstags kostet der Snooker Tisch<br>gerade mal 5€ die Stunde</p>
      </div>
    </section>

    <section class="special" style="top:492px">
      <div class="day-label">FREITAG</div>
      <div class="special-body">
        <h2 class="special-title">Kesselgold-Special</h2>
        <p class="special-text">6 Talhof Kesselgold-Pils für nur 11,99€</p>
      </div>
    </section>

    <section class="special" style="top:565px">
      <div class="day-label">SAMSTAG</div>
      <div class="special-body">
        <h2 class="special-title">Schau dein Wunschsspiel</h2>
        <p class="special-text">Reserviere die Private Lounge und schaue<br>das Staffelrunde-Spiel deiner Wahl.<br>Reservierungsgebühr: 10€,<br>ab 6 Personen kostenlos.<br><span class="special-note">(Gilt auch für EP, VKT-Pokal &amp; Englische Wochen)</span></p>
      </div>
    </section>

    <section class="special" style="top:718px">
      <div class="day-label">SONNTAG</div>
      <div class="special-body">
        <h2 class="special-title">Play for Free</h2>
        <p class="special-text">Wer vor 18:00 Uhr mit dem Spielen beginnt,<br>spielt den ganzen Abend umsonst!</p>
      </div>
    </section>
  </main>
</div>
</body>
</html>
```